Luxury Toilet Rental Business. Wavelet Hire.

Wavelet Hire (the logo is in the uploaded files)
We RENT and SELL Luxury Trailer toilets.
- Show location, number, pricing, pictures.
- We have two stall trailers for rent AND 3 stall trailers
- We sell them too
- We want our phone number shown
- We are a local company
- Slogan: Elevate your event with Wavelet Hire. The Luxurious Loo
- We want a pricing portion
- We want the sizes shown
- We want the different rates/ prices shown
- We do 1 day rentals
- We do 1 week rentals
- We want the service area. We serve Los Angeles County, Orange County, Riverside County, San Bernardino County, and Palm Desert.
- Our location is in Santa Ana California

Target Market(s)

Event planners, wedding planners, venue planners, concerts, events, gatherings.

Industry/Entity Type

Luxury Toilet Rentals

Number of Pages Required

1 page

Font styles to use
Serif
Sans Serif

Colors
EE7325
F08F49
F5BC92
FAE3D3
FDF4ED

Requirements
Must have
• Location, pricing, pictures, available areas. Our slogan.
Nice to have
• I like the idea of having tabs that show price, a tab that shows our contact information, pictures, event ideas, and where we service (the areas we'll go to)

```html
<!DOCTYPE html>
<html lang="en">
<head>
<meta charset="utf-8">
<title>Wavelet Hire — The Luxurious Loo</title>
<link href="https://fonts.googleapis.com/css2?family=Archivo+Black&family=Inter:wght@400;500;600;700&display=swap" rel="stylesheet">
<style>
:root{
  --stage:#3f3f41;
  --ink:#131313;
  --dark:#2e2d31;
  --dark-2:#35343a;
  --band:#4a494e;
  --orange:#ee7325;
  --orange-2:#f08f49;
  --peach:#f5bc92;
  --cream:#fae3d3;
  --white:#ffffff;
  --muted:#7a7a7a;
  --line:#dcdcdc;
}
*{box-sizing:border-box;margin:0;padding:0}
html,body{width:1200px;height:1200px;overflow:hidden;background:var(--stage)}
body{font-family:"Inter",sans-serif;color:var(--ink)}
.page{position:absolute;left:455px;top:51px;width:467px;height:1768px;background:var(--white);transform:scale(.6211);transform-origin:0 0;overflow:hidden}
.abs{position:absolute}
.display{font-family:"Archivo Black",sans-serif;text-transform:uppercase;letter-spacing:.4px;line-height:1.05}
.accent{color:var(--orange)}
.body-copy{font-size:4.2px;line-height:1.65;color:var(--muted)}
.photo{position:absolute;overflow:hidden}

/* hero */
.hero{left:0;top:0;width:467px;height:248px;background:linear-gradient(180deg,#29282c,var(--dark-2))}
.brand{font-family:"Archivo Black",sans-serif;font-size:10px;color:var(--white);letter-spacing:.5px;display:flex;align-items:center;gap:3px}
.brand .dot{width:5px;height:5px;background:var(--white)}
.call-btn{left:325px;top:8px;width:74px;height:19px;background:var(--orange);color:var(--white);display:flex;align-items:center;gap:6px;padding-left:6px}
.call-btn small{display:block;font-size:3.4px;font-weight:600}
.call-btn b{display:block;font-size:5px;font-weight:700}
.slogan-box{left:67px;top:62px;width:128px;height:116px;border:1px solid var(--white);text-align:center;color:var(--white)}
.slogan-box h1{font-size:13.5px;margin-top:19px}
.slogan-box .tag{position:absolute;left:14px;right:14px;bottom:-4px;background:#302f34;font-family:"Archivo Black",sans-serif;font-size:5.5px;letter-spacing:.3px}
.hero-photo{left:216px;top:58px;width:196px;height:212px;background:linear-gradient(180deg,#8e8e91 0%,#7d7d80 62%,#55555a 80%,#3d3d41 100%);box-shadow:0 10px 24px rgba(0,0,0,.35)}

/* product rows */
.frame{border:1.3px solid var(--orange);width:170px;height:155px}
.frame .photo{left:8px;top:7px;width:153px;height:139px}
.frame::after{content:"";position:absolute;left:45px;right:45px;bottom:-2px;height:3px;background:var(--white)}
.shot-two{background:linear-gradient(180deg,#d3d4d6 0%,#bdb8aa 38%,#8f9093 62%,#a7a7a5 100%)}
.shot-three{background:linear-gradient(180deg,#d7d8da 0%,#9b9c9f 30%,#85868a 70%,#5f9fb8 86%,#9a9a98 100%)}
.product h2{font-size:11px}
.product .body-copy{margin-top:9px;width:130px}
.tabs{display:flex;width:106px;margin-top:12px;font-size:3.6px;border-bottom:.6px solid var(--line)}
.tabs span{flex:1;text-align:center;padding-bottom:6px}
.tabs .on{color:var(--orange);border-bottom:1px solid var(--orange)}
.price{font-size:6.5px;font-weight:700;margin-top:10px}
.price-note{font-size:3.6px;color:var(--muted);margin-top:3px}
.btn{display:inline-flex;align-items:center;justify-content:center;background:var(--orange);color:var(--white);font-size:3.4px;font-weight:700;letter-spacing:.3px}
.product .btn{width:47px;height:14px;margin-top:12px}

/* locations */
.locations{left:30px;top:682px;width:437px;height:194px;background:linear-gradient(90deg,#4a494e,#3b3a3f)}
.locations h2{position:absolute;left:37px;top:36px;font-size:11px;color:var(--white)}
.locations .body-copy{position:absolute;left:37px;top:58px;width:150px;color:#c9c9c9}
.cities{position:absolute;left:37px;top:83px;display:flex;gap:9px}
.city{width:59px;font-size:4.6px;color:var(--white);font-weight:500;line-height:1.6}
.city .photo{position:relative;display:block;width:59px;height:60px;margin-bottom:4px}

/* local */
.local h2{font-size:11px}
.wordmark-faint{font-family:"Archivo Black",sans-serif;text-transform:uppercase;color:#f2f2f2;white-space:nowrap;letter-spacing:2px}
.gallery .photo{top:1008px;height:125px}

/* buy */
.buy-title{left:0;width:467px;top:1163px;text-align:center;font-size:26px;line-height:1.18}
.arrow{width:17px;height:17px;border:.6px solid var(--line);border-radius:50%;display:flex;align-items:center;justify-content:center}
.buy-price small{display:block;font-size:3.6px;color:var(--muted)}
.buy-price b{display:block;font-size:10px;color:var(--orange);font-weight:600;margin:1px 0 3px}
.buy-price em{font-style:normal;font-size:3.2px;color:#b5b5b5}

/* contact */
.contact-lead{font-size:8px;color:var(--white)}
.contact-title{font-size:11px;color:var(--orange)}
.call-line small{display:block;font-size:3.6px;color:var(--white);font-weight:600}
.call-line b{display:block;font-size:7.5px;color:var(--white);font-weight:700;letter-spacing:.3px;margin-top:2px}
.field{position:absolute;font-size:3.8px;color:#d0d0d0;border-bottom:.6px solid #77767b;padding-bottom:9px}
.lot-photo{left:67px;top:1352px;width:333px;height:190px;background:linear-gradient(180deg,#c7c9cb 0%,#b9ab86 30%,#a58f5c 46%,#8d8c8a 58%,#9c9c9b 80%,#8a8a8a 100%)}

/* footer */
.footer{left:0;top:1733px;width:467px;height:35px;background:var(--band)}
.copyright{font-size:3.6px;color:#e0e0e0}
.social{display:flex;gap:2px}
.social span{width:6px;height:6px;background:var(--orange)}
</style>
</head>
<body>
<main class="page">

  <header class="abs hero">
    <div class="abs brand" style="left:67px;top:11px"><span class="dot"></span>WAVELET HIRE</div>
    <a class="abs call-btn">
      <svg width="9" height="8" viewBox="0 0 24 20"><path fill="#fff" d="M2 6c0-3 4-5 10-5s10 2 10 5v2h-6V6c0-1-2-1-4-1s-4 0-4 1v2H2zM6 9h12l3 10H3z"/></svg>
      <span><small>CALL US</small><b>1800 555 010</b></span>
    </a>
    <div class="abs slogan-box">
      <h1 class="display">Elevate<br>your event<br>with<br><span class="accent">Wavelet<br>Hire</span></h1>
      <div class="tag">THE LUXURIOUS LOO</div>
    </div>
  </header>
  <div class="photo hero-photo" role="img" aria-label="Grey two stall luxury restroom trailer with steps"></div>

  <section class="product">
    <div class="abs frame" style="left:67px;top:290px">
      <div class="photo shot-two" role="img" aria-label="Two stall trailer parked outside a building"></div>
    </div>
    <div class="abs" style="left:257px;top:308px">
      <h2 class="display">Two stall<br>trailers</h2>
      <p class="body-copy">Spacious twin rooms with running water, vanity mirrors and climate control for any guest list.</p>
      <div class="tabs"><span class="on">1 Day</span><span>1 Week</span></div>
      <p class="price">$130</p>
      <p class="price-note">1 day rent (Time start from after reach at location)</p>
      <span class="btn">RENT NOW</span>
    </div>
  </section>

  <section class="product">
    <div class="abs" style="left:67px;top:497px">
      <h2 class="display">Three stall<br>trailers</h2>
      <p class="body-copy">Three private stalls with flush toilets, sinks and lighting, ideal for weddings and concerts.</p>
      <div class="tabs"><span class="on">1 Day</span><span>1 Week</span></div>
      <p class="price">$180</p>
      <p class="price-note">1 day rent (Time start from after reach at location)</p>
      <span class="btn">RENT NOW</span>
    </div>
    <div class="abs frame" style="left:237px;top:483px">
      <div class="photo shot-three" role="img" aria-label="Three stall trailer with blue steps"></div>
    </div>
  </section>

  <section class="abs locations">
    <h2 class="display">Location we serve</h2>
    <p class="body-copy">We deliver across Southern California, from the coast to the desert, for every kind of event.</p>
    <div class="cities">
      <div class="city"><span class="photo" role="img" aria-label="Los Angeles skyline" style="background:linear-gradient(180deg,#7fa9db 0%,#5a7291 55%,#3e4a58 100%)"></span>Los Angeles County</div>
      <div class="city"><span class="photo" role="img" aria-label="Orange County at sunset" style="background:linear-gradient(180deg,#f9c246 0%,#f08f2a 45%,#a4501f 100%)"></span>Orange County</div>
      <div class="city"><span class="photo" role="img" aria-label="Riverside aerial view" style="background:linear-gradient(180deg,#c9d0cb 0%,#8ea385 40%,#587346 100%)"></span>Riverside County</div>
      <div class="city"><span class="photo" role="img" aria-label="San Bernardino at dusk" style="background:linear-gradient(180deg,#5a7fc4 0%,#7b6f92 50%,#a8683e 100%)"></span>San Bernardino County</div>
      <div class="city"><span class="photo" role="img" aria-label="Palm Desert dunes" style="background:linear-gradient(180deg,#3a87dc 0%,#8db3d6 40%,#d9a35a 60%,#b9803f 100%)"></span>Palm Desert</div>
    </div>
  </section>

  <section class="local">
    <h2 class="abs display" style="left:67px;top:910px">We are local<br>company</h2>
    <p class="abs body-copy" style="left:240px;top:909px;width:130px">Based in Santa Ana, California, our team delivers, sets up and services every trailer ourselves, so your guests enjoy a clean, comfortable restroom from the first song to the last dance.</p>
    <div class="abs wordmark-faint" style="left:67px;top:968px;font-size:44px">WAVELET</div>
    <div class="gallery">
      <div class="photo" style="left:0;width:58px;background:linear-gradient(180deg,#e9e9e9 0%,#f6f6f6 45%,#d8d8d8 75%,#c9b491 100%)" role="img" aria-label="Trailer interior sink"></div>
      <div class="photo" style="left:67px;width:162px;background:linear-gradient(180deg,#e2e3e5 0%,#f3f3f3 45%,#dcdcdc 72%,#cdb48c 100%)" role="img" aria-label="Trailer interior with vanity and toilet"></div>
      <div class="photo" style="left:238px;width:105px;background:linear-gradient(180deg,#ececec 0%,#f7f7f7 50%,#e0e0e0 72%,#c8a97e 100%)" role="img" aria-label="Toilet and vanity cabinet"></div>
      <div class="photo" style="left:351px;width:105px;background:linear-gradient(180deg,#e6e6e6 0%,#f5f5f5 50%,#dedede 78%,#c6b08c 100%)" role="img" aria-label="Vanity basin close up"></div>
    </div>
  </section>

  <section class="buy">
    <h2 class="abs display buy-title">Buy <span class="accent">two stall</span><br>trailers</h2>
    <span class="abs arrow" style="left:83px;top:1238px"><svg width="6" height="4" viewBox="0 0 12 8"><path d="M11 4H1M4 1 1 4l3 3" stroke="#555" fill="none"/></svg></span>
    <span class="abs arrow" style="left:83px;top:1260px"><svg width="6" height="4" viewBox="0 0 12 8"><path d="M1 4h10M8 1l3 3-3 3" stroke="#555" fill="none"/></svg></span>
    <div class="abs buy-price" style="left:157px;top:1241px"><small>Price</small><b>$35,500</b><em>Tax excluded</em></div>
    <p class="abs body-copy" style="left:240px;top:1239px;width:122px">Own a two stall trailer outright. Fully fitted with flush toilets, sinks, lights and climate control, ready to tow to any venue and built for years of events.</p>
    <span class="abs btn" style="left:162px;top:1298px;width:140px;height:19px;font-size:4.2px">BUY NOW</span>
  </section>

  <section class="contact">
    <svg class="abs" style="left:0;top:1335px" width="467" height="400" viewBox="0 0 467 400"><path d="M0 63 Q233 -50 467 63 L467 400 L0 400Z" fill="#2f2e33"/></svg>
    <div class="photo lot-photo" role="img" aria-label="Trailer parked on a lot in front of a building"></div>
    <div class="abs wordmark-faint" style="left:0;top:1528px;font-size:40px;color:#3a393e;letter-spacing:3px">WAVELET HIRE</div>
    <p class="abs contact-lead" style="left:67px;top:1590px">Do You Have Any Query?</p>
    <h2 class="abs display contact-title" style="left:67px;top:1603px">Contact us</h2>
    <svg class="abs" style="left:67px;top:1632px" width="19" height="16" viewBox="0 0 24 20"><path fill="#fff" d="M2 6c0-3 4-5 10-5s10 2 10 5v2h-6V6c0-1-2-1-4-1s-4 0-4 1v2H2zM6 9h12l3 10H3z"/></svg>
    <div class="abs call-line" style="left:99px;top:1630px"><small>CALL US</small><b>1800 555 010</b></div>
    <div class="field" style="left:237px;top:1590px;width:77px">Name</div>
    <div class="field" style="left:322px;top:1590px;width:77px">Location</div>
    <div class="field" style="left:237px;top:1614px;width:77px">Email</div>
    <div class="field" style="left:322px;top:1614px;width:77px">Phone No</div>
    <div class="field" style="left:237px;top:1638px;width:162px;padding-bottom:22px">Your query</div>
    <span class="abs btn" style="left:237px;top:1675px;width:47px;height:14px">SUBMIT</span>
  </section>

  <footer class="abs footer">
    <div class="abs brand" style="left:67px;top:11px"><span class="dot"></span>WAVELET HIRE</div>
    <p class="abs copyright" style="left:237px;top:15px">Copyright ©2024 Wavelet Hire. All rights reserved.</p>
    <div class="abs social" style="left:375px;top:14px"><span></span><span></span><span></span></div>
  </footer>

</main>
</body>
</html>
```